VANTERLO needs a new Flyer Design

VANTERLO is the Continental Guild of Heritage Instructors and in 2017 it exists 25 years. The association has excelled at building bridges between history teachers across Europe and beyond through many projects, meetings, events and conferences. Another way of looking at history is that an open-minded attitude toward it can help build more democratic and peaceful societies. History does not stop at national/ethnic borders. More on our work is on www.vanterlo.eu.

It has recently obtained a celebratory 25 year anniversary logo, and we now want to update our flyer design and incorporate the new logo. We attach the new 25 year logo (in numerous versions) and the current flyer design. The new design should be fully based on the previous design.

Given we had added on a request for a business card design, please find attached our current business card design.

Target Market(s)

Teachers, Policy Makers, Foundations

Industry/Entity Type

Building

Contact Information for Business Card

VANTERLO address, Name and Surname, Role in organisation, Website, Social media accounts

Font styles to use
Sans Serif

Requirements
Must have
• -- new 25 year celebratory logo
• -- must be reasonably similar to the previous business card design (see attached)
• -- Colours used should be similar to those in the previous business card design (see attached)
• -- Font used should be similar to the font in the previous business card design (see attached)

```html
<!DOCTYPE html>
<html lang="en">
<head>
<meta charset="utf-8">
<title>VANTERLO Flyer</title>
<link href="https://fonts.googleapis.com/css2?family=Arimo:wght@400;700&display=swap" rel="stylesheet">
<style>
  :root {
    --navy: #1f4590;
    --band: #274a91;
    --white: #ffffff;
    --ink: #111111;
    --photo-a: #8fa7ad;
    --photo-b: #d6dde0;
    --badge: #c9ced8;
  }
  html, body { margin: 0; padding: 0; overflow: hidden; background: var(--white); }
  .flyer {
    position: relative; width: 1200px; height: 849px; overflow: hidden;
    background: var(--white); font-family: "Arimo", Arial, sans-serif; color: var(--ink);
  }
  .manifesto-title {
    position: absolute; left: 0; width: 399px; top: 93px; margin: 0;
    text-align: center; font-size: 22px; font-weight: 700; letter-spacing: 0.3px;
  }
  .manifesto-band {
    position: absolute; left: 0; top: 135px; width: 399px; height: 100px;
    background: var(--band); color: var(--white);
    display: flex; align-items: center; justify-content: center;
    text-align: center; font-size: 15px; line-height: 20px; white-space: nowrap;
  }
  .manifesto-intro {
    position: absolute; left: 50px; top: 253px; margin: 0; white-space: nowrap;
    font-size: 15px; line-height: 19px;
  }
  .manifesto-photo { position: absolute; left: 50px; top: 482px; width: 299px; height: 199px; }
  .manifesto-link {
    position: absolute; left: 50px; top: 729px; margin: 0; white-space: nowrap;
    font-size: 15px; line-height: 21px;
  }
  .contact-block {
    position: absolute; left: 399px; top: 0; width: 801px; height: 549px; background: var(--navy);
  }
  .secretariat {
    position: absolute; left: 370px; top: 215px; width: 440px; white-space: nowrap;
    text-align: center; color: var(--white); font-weight: 700; font-size: 15.5px; line-height: 18px;
  }
  .secretariat p { margin: 0 0 22px; }
  .frame-top {
    position: absolute; left: 845px; top: 48px; width: 312px; height: 501px;
    border: 2px solid var(--white); border-bottom: none; box-sizing: border-box;
  }
  .frame-bottom {
    position: absolute; left: 845px; top: 549px; width: 312px; height: 256px;
    border: 2px solid var(--navy); border-top: none; box-sizing: border-box;
  }
  .headline {
    position: absolute; left: 871px; top: 190px; width: 280px; margin: 0;
    color: var(--white); font-weight: 700; font-size: 42px; line-height: 51px;
  }
  .partner-badge { position: absolute; background: var(--badge); }
  .disclaimer {
    position: absolute; left: 434px; top: 662px; margin: 0; white-space: nowrap;
    font-size: 10.3px; line-height: 14.5px;
  }
  .brand {
    position: absolute; left: 876px; top: 716px; display: flex; align-items: center; gap: 10px;
    color: var(--navy); font-weight: 700; font-size: 30px; letter-spacing: 0.5px;
  }
  .brand-dot { width: 34px; height: 34px; border-radius: 50%; background: var(--navy); }
</style>
</head>
<body>
<div class="flyer">
  <h2 class="manifesto-title">OUR MANIFESTO</h2>
  <div class="manifesto-band">15 Principles for the distinctive<br>contribution of history to the development<br>of young people</div>
  <p class="manifesto-intro">In 2014, the general assembly of<br>VANTERLO unanimously adopted a<br>manifesto with principles for<br>high-quality history, heritage and<br>citizenship education. This manifesto on<br>preventing the misuses of the past,<br>promoting an inclusive approach to the<br>study of the past and advancing<br>educational innovation.</p>
  <svg class="manifesto-photo" role="img" aria-label="Photograph of printed manifesto pages" viewBox="0 0 299 199">
    <defs>
      <linearGradient id="photoTone" x1="0" y1="0" x2="1" y2="1">
        <stop offset="0" stop-color="var(--photo-a)"/>
        <stop offset="1" stop-color="var(--photo-b)"/>
      </linearGradient>
    </defs>
    <rect width="299" height="199" fill="url(#photoTone)"/>
  </svg>
  <p class="manifesto-link">The manifesto is available in multiple<br>languages at www.vanterlo.eu/manifesto</p>

  <div class="contact-block"></div>
  <div class="secretariat">
    <p>VANTERLO Secretariat</p>
    <p>Lindenkade 42</p>
    <p>2514 AB, The Hague, The Netherlands</p>
    <p>www.vanterlo.eu, secretariat@vanterlo.eu</p>
  </div>

  <div class="frame-top"></div>
  <div class="frame-bottom"></div>
  <h1 class="headline">HOW CAN HISTORY TEACHING CHANGE TODAY?</h1>

  <div class="partner-badge" style="left:449px;top:596px;width:138px;height:34px;"></div>
  <div class="partner-badge" style="left:613px;top:599px;width:125px;height:29px;"></div>
  <p class="disclaimer">This flyer is made with the support of the Shared Past Dialogue<br>programme of the Northwind Alliance and the Classroom Bridges<br>Programme of the Brightwater Trust Foundations.<br>The Alliance Board support for the production of this<br>publication does not constitute an endorsement of the contents<br>which reflects the views only of the authors, and the<br>Board cannot be held responsible for any use which may<br>be made of the information contained therein.</p>

  <div class="brand"><span class="brand-dot"></span><span>VANTERLO</span></div>
</div>
</body>
</html>
```